Plakat-Design für Verkauf von Bio-zertifiziertem Saatgut
Zielgruppe
Wir sind ein Start Up und verkaufen BIO Zertifiziertes Saatgut für Gemüse, Kräuter, Heilpflanzen und essbare Sprossen etc. Zielgruppe ist vor allem die DIY Community von Jung bis Alt.
Aufgabenstellung
*** INFO*** Da es keine 'Kalender'-Projekte gibt, sollten wir das Projekt unter 'Plakat' einstellen ***INFO***
Wir sind auf der Suche nach einem Design für einen Monatskalender (Deckblatt, 12 Monate, Schlussblatt) der als ewiger Aussaatkalender fungieren soll (Keine Jahreszahlen, nur der Monat). Jeden Monat sollen die Sorten gezeigt werden die jetzt ausgesät werden können. Am Besten teilweise (nicht alle) als Illustrationen oder Bilder. Die Sorten orientieren sich an unserem Saatgutsortiment. Als Unterteilung kann man: 'Vorzucht im Haus', Frühbeet' und 'Direktsaat'
Die Informationen welche Samen wann ausgesät werden, kommen von uns. (Erstmal Platzhalter für das Design nutzen) Falls der Designer Erfahrung in diesem Bereich hat, kann er die Informationen auch selber einfügen. Sonst ist der Designer für Layout und Illustrationen/Bilder zuständig. Toll wäre wenn für jeden Monat noch eine 'Bauernweisheit' zum Thema Pflanzen / Aussaat / Garten hinzugefügt werden kann.
Das Design soll sich an unserer CI der Website www.keimfeld.de orientieren. Logo, Farben und Fonts (My-Everything, BW Mitga) sind im Anhang beigefügt. Auch die Vorlage der Druckerei ist beigefügt. Format: DIN A4 hoch (210 x 297 mm), beidseitig bedruckt so das man den Kalender auch Aufgeklappt nutzen kann.
Falls noch Informationen benötigt werden, dann meldet euch gerne!

```html
<!DOCTYPE html>
<html lang="de">
<head>
<meta charset="utf-8">
<title>Keimfeld – Saatgut Kalender Deckblatt</title>
<link rel="stylesheet" href="https://fonts.googleapis.com/css2?family=Montserrat:wght@600;800&family=Mulish:wght@700&family=Mrs+Saint+Delafield&display=swap">
<style>
  :root {
    --brand-green: #5b7f38;
    --script-brown: #4a2a12;
    --paper: #fbf6f1;
    --wash-mint: #b9dfc8;
    --wash-peach: #f6d9bd;
    --wash-coral: #f4a98a;
    --wash-sand: #efe3d6;
    --rule: #9fb384;
    --page-bg: #ffffff;
  }
  * { margin: 0; padding: 0; box-sizing: border-box; }
  html, body {
    width: 1200px; height: 1200px; overflow: hidden;
    background: var(--page-bg);
  }
  .cover {
    position: absolute; left: 208px; top: 47px;
    width: 784px; height: 1107px;
    background: var(--paper);
    overflow: hidden;
  }
  .cover__wash {
    position: absolute; inset: 0;
    background:
      radial-gradient(ellipse 260px 150px at 140px 70px, var(--wash-mint) 0%, rgba(185,223,200,0.6) 55%, rgba(185,223,200,0) 100%),
      radial-gradient(ellipse 300px 260px at 560px 260px, rgba(239,227,214,0.9) 0%, rgba(239,227,214,0) 100%),
      radial-gradient(ellipse 200px 320px at 80px 540px, rgba(246,217,189,0.85) 0%, rgba(246,217,189,0) 100%),
      radial-gradient(ellipse 380px 360px at 560px 620px, rgba(248,225,208,0.8) 0%, rgba(248,225,208,0) 100%),
      radial-gradient(ellipse 260px 300px at 720px 1020px, var(--wash-coral) 0%, rgba(244,169,138,0.45) 50%, rgba(244,169,138,0) 100%),
      radial-gradient(ellipse 260px 160px at 250px 1020px, rgba(226,232,216,0.8) 0%, rgba(226,232,216,0) 100%),
      var(--paper);
  }
  .cover__brand {
    position: absolute; left: 0; right: 0; top: 240px;
    text-align: center;
    font-family: "Montserrat", sans-serif;
    font-weight: 600; font-size: 38px; letter-spacing: 5px;
    color: var(--brand-green);
  }
  .cover__title {
    position: absolute; left: 0; right: 0; top: 498px;
    text-align: center;
    font-family: "Montserrat", sans-serif;
    font-weight: 800; font-size: 104px; letter-spacing: 4px; line-height: 1;
    color: var(--brand-green);
  }
  .cover__subtitle {
    position: absolute; left: 0; right: 0; top: 585px;
    text-align: center;
    font-family: "Mrs Saint Delafield", cursive;
    font-size: 96px; line-height: 1;
    color: var(--script-brown);
  }
  .cover__rule {
    position: absolute; left: 256px; top: 902px;
    width: 270px; height: 1px;
    background: var(--rule);
  }
  .cover__intro {
    position: absolute; left: 200px; top: 936px; width: 384px;
    text-align: center;
    font-family: "Mulish", sans-serif;
    font-weight: 700; font-size: 13px; line-height: 18.5px; letter-spacing: 0.5px;
    color: var(--brand-green);
  }
</style>
</head>
<body>
  <main class="cover">
    <div class="cover__wash" role="img" aria-label="Aquarell-Hintergrund in Mintgrün, Pfirsich und Koralle"></div>
    <div class="cover__brand">KEIMFELD</div>
    <h1 class="cover__title">SAATGUT</h1>
    <div class="cover__subtitle">Kalender</div>
    <div class="cover__rule"></div>
    <p class="cover__intro">Lorem ipsum dolor sit amet, consectetuer adipis-<br>cing elit, sed diam nonummy nibh euismod tincid-<br>unt ut laoreet dolore</p>
  </main>
</body>
</html>
```